New Business Card for Auto Repair and Performance Shop!

Need a redesign on a card that we have used for a while now. Something more update and modern, Serious but not too serious. Something confident, that shows the client that we are bespoke. Adding value.

Target Market(s)

Foreign Auto Repair and Performance

Industry/Entity Type

Automotive

Contact Information for Business Card

Utilize Logo, would like to change car silhouette to something Veltra,

Font styles to use
Sans Serif

Requirements
Must have
• business name, address, website, phone number.
MotoSerenix
4918 W. Birchwell Rd
Ridgeford, T.X. 70418
1-254-487-3106
www.moto-serenix-example.com

Specializing in Asian, European, and Domestic Auto Repair, Performance and Fabrication.

Clear space on back to for space to write appointment time and which client advisor helped the client.
Nice to have
• Up to the designers,

```html
<!DOCTYPE html>
<html lang="en">
<head>
<meta charset="utf-8">
<title>MotoSerenix Business Card</title>
<link rel="stylesheet" href="https://fonts.googleapis.com/css2?family=Roboto+Condensed:wght@700&family=Saira:wght@500;700;800&display=swap">
<style>
  :root {
    --stage: #1c1c1e;
    --card: #141416;
    --card-edge: #222226;
    --red: #e41f26;
    --white: #ffffff;
  }
  * { box-sizing: border-box; margin: 0; padding: 0; }
  html, body { width: 1200px; height: 900px; overflow: hidden; }
  body {
    background: radial-gradient(ellipse at 50% 40%, #2c2c2f 0%, var(--stage) 70%);
    font-family: "Saira", sans-serif;
    color: var(--white);
    position: relative;
  }
  .card {
    position: absolute;
    left: 285px;
    width: 630px;
    height: 360px;
    background: linear-gradient(160deg, var(--card-edge) 0%, var(--card) 60%);
    box-shadow: 0 18px 40px rgba(0,0,0,.55);
    overflow: hidden;
  }
  .card--back { top: 60px; }
  .card--front { top: 480px; }

  .wordmark {
    display: flex;
    align-items: center;
    gap: 12px;
    font-weight: 800;
    color: var(--white);
    letter-spacing: 1px;
    white-space: nowrap;
  }
  .wordmark__square { background: var(--red); flex: none; }

  /* back */
  .card--back .wordmark {
    justify-content: center;
    font-size: 48px;
    margin-top: 44px;
  }
  .card--back .wordmark__square { width: 34px; height: 34px; }
  .tagline {
    text-align: center;
    font-family: "Roboto Condensed", sans-serif;
    font-weight: 700;
    font-size: 14px;
    letter-spacing: 2.6px;
    text-transform: uppercase;
    line-height: 1.35;
    margin-top: 14px;
  }
  .field {
    margin: 0 40px;
    height: 40px;
    background: var(--white);
    color: #111;
    font-weight: 700;
    font-size: 17px;
    padding: 6px 14px;
  }
  .field--name { margin-top: 22px; }
  .field--date { margin-top: 12px; }
  .back-accent {
    position: absolute;
    bottom: 0;
    left: 50%;
    transform: translateX(-50%);
    width: 90px;
    height: 8px;
    background: var(--red);
  }

  /* front */
  .front-brand {
    position: absolute;
    left: 30px;
    top: 138px;
    font-size: 36px;
    gap: 10px;
  }
  .front-brand .wordmark__square { width: 28px; height: 28px; }
  .divider {
    position: absolute;
    left: 318px;
    top: 60px;
    width: 2px;
    height: 200px;
    background: var(--red);
  }
  .contact {
    position: absolute;
    left: 336px;
    top: 62px;
    right: 12px;
    white-space: nowrap;
  }
  .contact__name {
    color: var(--red);
    font-weight: 800;
    font-size: 25px;
    text-transform: uppercase;
    line-height: 1.05;
  }
  .contact__role {
    font-weight: 700;
    font-size: 20px;
    margin-bottom: 14px;
  }
  .contact__line {
    display: flex;
    align-items: center;
    gap: 8px;
    font-weight: 700;
    font-size: 18px;
    line-height: 1.5;
  }
  .contact__line--web { font-size: 14.5px; }
  .contact__icon { width: 20px; height: 20px; flex: none; }
  .contact__address {
    margin-top: 16px;
    font-weight: 700;
    font-size: 20px;
    line-height: 1.2;
  }
  .front-stripe {
    position: absolute;
    left: 0; right: 0; bottom: 0;
    height: 12px;
    background: linear-gradient(to right, var(--white) 0 45%, var(--red) 45% 55%, var(--white) 55% 100%);
  }
</style>
</head>
<body>

  <section class="card card--back" aria-label="Card back">
    <div class="wordmark">
      <span class="wordmark__square"></span>
      <span class="wordmark__name">MotoSerenix</span>
    </div>
    <p class="tagline">Specializing in Asian, European<br>and Domestic Auto Repair, Performance and Fabrication.</p>
    <div class="field field--name">Name:</div>
    <div class="field field--date">Date/ Time:</div>
    <span class="back-accent"></span>
  </section>

  <section class="card card--front" aria-label="Card front">
    <div class="wordmark front-brand">
      <span class="wordmark__square"></span>
      <span class="wordmark__name">MotoSerenix</span>
    </div>
    <span class="divider"></span>
    <div class="contact">
      <p class="contact__name">Marcus Delgado</p>
      <p class="contact__role">Managing Partner</p>
      <p class="contact__line">
        <svg class="contact__icon" viewBox="0 0 20 20" aria-hidden="true">
          <rect width="20" height="20" fill="#e41f26"/>
          <path d="M6 4.5c.8 0 1.4 2 1.4 2.6 0 .7-1 1-1 1.5.4 1.6 2.4 3.6 4 4 .5 0 .8-1 1.5-1 .6 0 2.6.6 2.6 1.4 0 .9-1.2 2.5-2.5 2.5C8.5 15.5 4.5 11.5 4.5 7 4.5 5.7 5.1 4.5 6 4.5z" fill="#fff"/>
        </svg>
        <span>1-254-487-3106</span>
      </p>
      <p class="contact__line contact__line--web">
        <svg class="contact__icon" viewBox="0 0 20 20" aria-hidden="true">
          <circle cx="10" cy="10" r="8" fill="#e41f26"/>
          <g fill="none" stroke="#fff" stroke-width="1.2">
            <circle cx="10" cy="10" r="6"/>
            <ellipse cx="10" cy="10" rx="2.6" ry="6"/>
            <path d="M4 10h12M5 7h10M5 13h10"/>
          </g>
        </svg>
        <span>www.moto-serenix-example.com</span>
      </p>
      <p class="contact__address">4918 W. Birchwell Rd<br>Ridgeford, T.X. 70418</p>
    </div>
    <span class="front-stripe"></span>
  </section>

</body>
</html>
```